Business Card, Stationary, Envelope
Biz Cd/Stationary 4 ClinicPathwise
Business Card, Stationary, Envelope -
Creative Brief
Professional
Derek Sorvano
President
387 Harmon Ridge, #2214 Willowbrook, IL 60419
dsorvano@ClinicPathwise-example.com
www.ClinicPathwise-example.com
Clean appearance for medical practice consulting firm... tagline is "Evaluate. Implement. Thrive." although not sure that will fit on card. FYI....Skills of corporation are performance improvement, information systems evaluation. change emnagement, leadership, marketing...so kind of looking for kind of cutting edge/forward thinking, but definitely professional appearance

```html
<!DOCTYPE html>
<html lang="en">
<head>
<meta charset="utf-8">
<title>ClinicPathwise Stationery</title>
<link rel="stylesheet" href="https://fonts.googleapis.com/css2?family=Open+Sans:wght@400;600;700&display=swap">
<style>
  :root {
    --stage: #3b3b3b;
    --paper: #ffffff;
    --paper-shade: #f1f3f4;
    --brand-blue: #1f86d3;
    --brand-blue-light: #6fb8ea;
    --brand-green: #5db52f;
    --brand-green-light: #9bd46f;
    --ink: #4d4d4d;
    --ink-soft: #8a8a8a;
  }
  * { box-sizing: border-box; margin: 0; padding: 0; }
  html, body { width: 1200px; height: 602px; overflow: hidden; }
  body {
    background: var(--stage);
    font-family: "Open Sans", Arial, sans-serif;
    color: var(--ink);
    position: relative;
  }
  .wordmark {
    font-family: "Open Sans", Arial, sans-serif;
    font-weight: 600;
    color: var(--brand-blue);
    display: flex;
    align-items: center;
    gap: 4px;
    line-height: 1;
    white-space: nowrap;
  }
  .wordmark .dot { width: 6px; height: 6px; border-radius: 50%; background: var(--brand-green); }

  /* Business card */
  .business-card {
    position: absolute; left: 12px; top: 308px; width: 138px; height: 124px;
    background: var(--paper); border-radius: 8px; overflow: hidden;
    box-shadow: 0 3px 8px rgba(0,0,0,.45);
  }
  .business-card .edge-band { position: absolute; left: 0; top: 0; bottom: 0; width: 7px; background: linear-gradient(var(--brand-blue-light), var(--brand-blue)); }
  .business-card .wordmark { position: absolute; left: 16px; top: 22px; font-size: 12.5px; }
  .business-card .tagline { position: absolute; left: 30px; top: 37px; font-size: 4.5px; color: var(--brand-green); letter-spacing: .3px; }
  .business-card .person { position: absolute; left: 16px; top: 58px; font-size: 5px; line-height: 1.3; }
  .business-card .person strong { color: var(--brand-blue); font-weight: 600; display: block; }
  .business-card .contact { position: absolute; left: 16px; top: 78px; font-size: 3.6px; line-height: 1.5; color: var(--ink); }
  .contact-line { display: flex; align-items: center; gap: 2px; }
  .contact-line i { width: 3px; height: 3px; border-radius: 50%; background: var(--brand-green); display: inline-block; }

  /* Letterhead */
  .letterhead {
    position: absolute; left: 228px; top: 30px; width: 384px; height: 552px;
    background: var(--paper); box-shadow: 0 4px 12px rgba(0,0,0,.5);
  }
  .letterhead .edge-band { position: absolute; left: 0; top: 0; bottom: 0; width: 9px; background: linear-gradient(90deg, var(--brand-blue), var(--brand-blue-light)); }
  .letterhead .wordmark { position: absolute; left: 26px; top: 22px; font-size: 17px; }
  .letterhead .tagline { position: absolute; left: 44px; top: 41px; font-size: 5px; color: var(--brand-green); letter-spacing: .4px; }
  .letterhead .person { position: absolute; left: 212px; top: 22px; font-size: 5px; line-height: 1.4; text-align: right; width: 40px; }
  .letterhead .person strong { color: var(--brand-blue); font-weight: 600; display: block; }
  .letterhead .divider { position: absolute; left: 257px; top: 20px; width: 1px; height: 34px; background: #cfcfcf; }
  .letterhead .contact { position: absolute; left: 263px; top: 20px; font-size: 4px; line-height: 1.6; }
  .letterhead .footer-url { position: absolute; left: 0; right: 0; bottom: 10px; text-align: center; font-size: 5px; color: var(--ink); }

  /* Envelopes */
  .envelope-back { position: absolute; left: 684px; width: 510px; height: 190px; filter: drop-shadow(0 4px 6px rgba(0,0,0,.45)); }
  .envelope-back.green { top: 48px; }
  .envelope-back.blue { top: 178px; }
  .envelope-back.white { top: 276px; }

  .envelope-front {
    position: absolute; left: 516px; top: 326px; width: 312px; height: 142px;
    background: var(--paper); box-shadow: 0 4px 10px rgba(0,0,0,.5); overflow: hidden;
  }
  .envelope-front .edge-band { position: absolute; left: 0; top: 0; bottom: 0; width: 5px; background: linear-gradient(var(--brand-blue-light), var(--brand-blue)); }
  .envelope-front .wordmark { position: absolute; left: 14px; top: 14px; font-size: 11px; }
  .envelope-front .return-address { position: absolute; left: 14px; top: 32px; font-size: 3.6px; color: var(--ink-soft); }
</style>
</head>
<body>

  <svg class="envelope-back green" viewBox="0 0 510 190" aria-hidden="false">
    <defs>
      <linearGradient id="flapGreen" x1="0" y1="0" x2="0" y2="1">
        <stop offset="0" stop-color="#9bd46f"/><stop offset="1" stop-color="#4ea826"/>
      </linearGradient>
    </defs>
    <rect x="0" y="0" width="510" height="190" fill="#f4f5f5"/>
    <path d="M0 0 H510 V40 Q255 150 0 40 Z" fill="url(#flapGreen)"/>
    <text x="262" y="58" font-family="Open Sans, sans-serif" font-weight="600" font-size="11" fill="#ffffff">ClinicPathwise</text>
  </svg>

  <svg class="envelope-back blue" viewBox="0 0 510 190">
    <defs>
      <linearGradient id="flapBlue" x1="0" y1="0" x2="0" y2="1">
        <stop offset="0" stop-color="#6fb8ea"/><stop offset="1" stop-color="#1a78c2"/>
      </linearGradient>
    </defs>
    <rect x="0" y="0" width="510" height="190" fill="#f4f5f5"/>
    <path d="M0 0 H510 V30 Q255 140 0 30 Z" fill="url(#flapBlue)"/>
    <text x="262" y="52" font-family="Open Sans, sans-serif" font-weight="600" font-size="11" fill="#ffffff">ClinicPathwise</text>
  </svg>

  <svg class="envelope-back white" viewBox="0 0 510 190">
    <rect x="0" y="0" width="510" height="190" fill="#f7f8f8"/>
    <path d="M0 0 H510 V30 Q255 140 0 30 Z" fill="#ffffff" stroke="#dddddd"/>
    <text x="262" y="56" font-family="Open Sans, sans-serif" font-weight="600" font-size="11" fill="#1f86d3">ClinicPathwise</text>
    <text x="262" y="66" font-family="Open Sans, sans-serif" font-size="4" fill="#8a8a8a">www.ClinicPathwise-example.com</text>
  </svg>

  <section class="letterhead">
    <div class="edge-band"></div>
    <div class="wordmark"><span class="dot"></span>ClinicPathwise</div>
    <div class="tagline">Evaluate. Implement. Thrive.</div>
    <div class="person"><strong>Derek Sorvano</strong>President</div>
    <div class="divider"></div>
    <div class="contact">
      <div>387 Harmon Ridge, #2214</div>
      <div>Willowbrook, IL 60419</div>
      <div class="contact-line"><i></i>(630) 555-0148</div>
      <div class="contact-line"><i></i>dsorvano@ClinicPathwise-example.com</div>
    </div>
    <div class="footer-url">www.ClinicPathwise-example.com</div>
  </section>

  <section class="envelope-front">
    <div class="edge-band"></div>
    <div class="wordmark"><span class="dot"></span>ClinicPathwise</div>
    <div class="return-address">387 Harmon Ridge, #2214 Willowbrook, IL 60419</div>
  </section>

  <section class="business-card">
    <div class="edge-band"></div>
    <div class="wordmark"><span class="dot"></span>ClinicPathwise</div>
    <div class="tagline">Evaluate. Implement. Thrive.</div>
    <div class="person"><strong>Derek Sorvano</strong>President</div>
    <div class="contact">
      <div>387 Harmon Ridge, #2214</div>
      <div>Willowbrook, IL 60419</div>
      <div class="contact-line"><i></i>(630) 555-0148</div>
      <div class="contact-line"><i></i>dsorvano@ClinicPathwise-example.com</div>
      <div class="contact-line"><i></i>www.ClinicPathwise-example.com</div>
    </div>
  </section>

</body>
</html>
```